Product flyer with pricing

We manufacture iconic and luxury vending trailers. for our first trailer we need a flyer created to give to prospective clients with base pricing. I am uploading an example along with graphic files.

```html
<!DOCTYPE html>
<html lang="en">
<head>
<meta charset="utf-8">
<title>Country Cottage Mini – Product Flyer</title>
<link href="https://fonts.googleapis.com/css2?family=Poppins:wght@300;400;500;600;700;800&display=swap" rel="stylesheet">
<style>
  :root {
    --green: #62a846;
    --yellow: #f0b429;
    --ink: #5a5a5a;
    --ink-soft: #6b6b6b;
    --paper: #ffffff;
    --backdrop: #e4e4e4;
    --sky: #6f9fd6;
    --asphalt: #3d3f44;
  }
  * { box-sizing: border-box; margin: 0; padding: 0; }
  html, body { width: 1200px; height: 1200px; overflow: hidden; }
  body {
    background: var(--backdrop);
    font-family: "Poppins", sans-serif;
    color: var(--ink);
    position: relative;
  }
  .flyer {
    position: absolute;
    left: 151px; top: 20px;
    width: 897px; height: 1160px;
    background: var(--paper);
  }
  .abs { position: absolute; }

  .title-bar {
    left: 31px; top: 32px; width: 580px; height: 58px;
    background: var(--green);
    color: #fff; font-weight: 800; font-size: 33px;
    line-height: 58px; padding-left: 24px; letter-spacing: 0.2px;
    white-space: nowrap;
  }
  .subtitle {
    left: 29px; top: 92px;
    font-weight: 300; font-size: 36.5px; color: var(--ink-soft);
    white-space: nowrap; letter-spacing: 0.3px;
  }
  .brand {
    left: 700px; top: 62px; width: 170px;
    display: flex; align-items: center; gap: 8px;
  }
  .brand-dot { width: 16px; height: 16px; border-radius: 50%; background: var(--yellow); flex: none; }
  .brand-name { font-weight: 700; font-size: 19px; line-height: 1.15; color: var(--green); }

  .photo { background: linear-gradient(180deg, var(--sky) 0%, #b9cfe6 40%, #f2f2f2 55%, #e9e9e9 72%, var(--asphalt) 100%); }
  .photo-front { left: 26px; top: 154px; width: 370px; height: 435px; }
  .photo-side { left: 404px; top: 154px; width: 232px; height: 210px; }
  .photo-rear { left: 644px; top: 154px; width: 225px; height: 210px; }
  .photo-window { left: 404px; top: 373px; width: 232px; height: 216px; }

  .price-box {
    left: 644px; top: 373px; width: 225px; height: 216px;
    background: var(--yellow); color: #fff;
    text-align: center; font-weight: 800;
    padding-top: 36px;
  }
  .price-box .label { font-size: 36px; line-height: 40px; }
  .price-box .amount { font-size: 41px; line-height: 46px; margin-top: 0; }
  .price-box .rule { width: 62px; height: 2px; background: #fff; margin: 16px auto 0; }

  .section-head { font-size: 23px; line-height: 25px; }
  .section-head strong { display: block; color: var(--green); font-weight: 800; }
  .section-head span { display: block; font-weight: 400; color: var(--ink-soft); }
  .features-head { left: 29px; top: 608px; }
  .options-head { left: 482px; top: 608px; }

  .feature-list { left: 30px; top: 676px; width: 350px; list-style: none; }
  .feature-list li {
    display: flex; gap: 12px; font-size: 13px; line-height: 16.5px;
    margin-bottom: 12px; color: var(--ink);
  }
  .feature-list svg { flex: none; width: 16px; height: 16px; margin-top: 0; }

  .divider { width: 2px; background: linear-gradient(180deg, transparent, #c9c9c9 20%, #c9c9c9 80%, transparent); }
  .divider-upper { left: 566px; top: 614px; height: 290px; transform: translateX(-120px); }
  .divider-lower { left: 446px; top: 1000px; height: 120px; }

  .option-list { left: 482px; top: 676px; width: 384px; list-style: none; }
  .option-list li {
    display: flex; justify-content: space-between; align-items: flex-start;
    font-size: 13px; line-height: 16.5px; margin-bottom: 12px;
  }
  .option-list .price {
    width: 123px; height: 22px; background: var(--green); color: #fff;
    font-weight: 600; font-size: 12.5px; line-height: 22px; text-align: center; flex: none;
  }

  .uc-line { left: 0; top: 963px; width: 897px; height: 2px; background: var(--yellow); }
  .uc-tab {
    left: 326px; top: 948px; width: 243px; height: 32px;
    background: var(--yellow); color: #fff; text-align: center;
    font-size: 21px; line-height: 32px;
    box-shadow: 0 8px 8px -6px rgba(90,60,140,0.35);
  }
  .uc-tab strong { font-weight: 800; }
  .uc-tab span { font-weight: 400; }

  .use-case { display: flex; gap: 14px; width: 330px; }
  .use-case svg { width: 48px; height: 48px; flex: none; }
  .use-case h3 { font-size: 13.5px; line-height: 16px; font-weight: 700; color: var(--green); }
  .use-case p { font-size: 13px; line-height: 16.5px; }
  .uc-food { left: 31px; top: 1001px; }
  .uc-retail { left: 31px; top: 1063px; }
  .uc-corporate { left: 483px; top: 1001px; }
  .uc-fundraisers { left: 483px; top: 1063px; }

  .footer-bar { left: 31px; top: 1145px; width: 833px; height: 15px; background: var(--green); }
</style>
</head>
<body>
<svg width="0" height="0" style="position:absolute">
  <defs>
    <symbol id="tick" viewBox="0 0 16 16">
      <path d="M14 7.2A6 6 0 1 1 10.6 2.4" fill="none" stroke="#62a846" stroke-width="1.6" stroke-linecap="round"/>
      <path d="M5 7.6l2.6 2.6L14.2 3.4" fill="none" stroke="#62a846" stroke-width="1.6" stroke-linecap="round" stroke-linejoin="round"/>
    </symbol>
    <symbol id="ring" viewBox="0 0 48 48">
      <path d="M24 3A21 21 0 0 0 24 45" fill="none" stroke="#62a846" stroke-width="3.5"/>
      <path d="M24 3A21 21 0 0 1 24 45" fill="none" stroke="#f0b429" stroke-width="3.5"/>
    </symbol>
  </defs>
</svg>

<main class="flyer">
  <h1 class="abs title-bar">THE &ldquo;COUNTRY COTTAGE MINI&rdquo;</h1>
  <h2 class="abs subtitle">LUXURY, MOBILE VENDING HOUSE</h2>

  <div class="abs brand">
    <span class="brand-dot"></span>
    <span class="brand-name">Bright Nook Builds</span>
  </div>

  <div class="abs photo photo-front" role="img" aria-label="Front view of the white board-and-batten vending house with black door and window"></div>
  <div class="abs photo photo-side" role="img" aria-label="Side view of the vending trailer on tandem wheels with serving window"></div>
  <div class="abs photo photo-rear" role="img" aria-label="Three-quarter view of the vending house hitched to a truck"></div>
  <div class="abs photo photo-window" role="img" aria-label="Serving window being opened on the side of the trailer"></div>

  <div class="abs price-box">
    <div class="label">BASE<br>PRICE</div>
    <div class="amount">$45,000</div>
    <div class="rule"></div>
  </div>

  <h3 class="abs section-head features-head"><strong>BASE</strong><span>UNIT FEATURES</span></h3>
  <ul class="abs feature-list">
    <li><svg><use href="#tick"/></svg>Trailer features tandem wheels w/ brakes</li>
    <li><svg><use href="#tick"/></svg>Steel frame construction for fire retardation safety and weight reduction.</li>
    <li><svg><use href="#tick"/></svg>100% off grid with solar and lithium battery system allowing the trailer to be used in places not accessible by traditional trailers.</li>
    <li><svg><use href="#tick"/></svg>80 gallon water supply tank</li>
    <li><svg><use href="#tick"/></svg>100 gallon waste water tank</li>
    <li><svg><use href="#tick"/></svg>Cupboards, cabinets &amp; four stainless steel sinks.</li>
    <li><svg><use href="#tick"/></svg>60&rdquo; Gas shock serving window</li>
  </ul>

  <div class="abs divider divider-upper"></div>

  <h3 class="abs section-head options-head"><strong>AVAILABLE</strong><span>OPTIONS</span></h3>
  <ul class="abs option-list">
    <li><span>HVAC - Kelvo Mini Split</span><span class="price">$1,800</span></li>
    <li><span>Cooler / Glass front<br>Commercial refrigerator</span><span class="price">$1,600</span></li>
    <li><span>Upper loft storage area</span><span class="price">$1,200</span></li>
    <li><span>Signage and graphics<br>depend on complexity</span><span class="price">$2,000 - $5,000</span></li>
    <li><span>Ice machine</span><span class="price">$1,100</span></li>
    <li><span>Other custom items available on request</span></li>
  </ul>

  <div class="abs uc-line"></div>
  <div class="abs uc-tab"><strong>USE</strong> <span>CASES</span></div>

  <div class="abs use-case uc-food">
    <svg viewBox="0 0 48 48"><use href="#ring"/><path d="M18 20h12l-1.5 14h-9z" fill="none" stroke="#777" stroke-width="1.4"/><path d="M24 20v-5l3-2" fill="none" stroke="#777" stroke-width="1.4"/></svg>
    <div><h3>Food</h3><p>Lemonade, Coffee, pizza, cookies, doughnuts, barbecue and more!</p></div>
  </div>
  <div class="abs use-case uc-retail">
    <svg viewBox="0 0 48 48"><use href="#ring"/><rect x="17" y="21" width="14" height="13" fill="none" stroke="#777" stroke-width="1.4"/><path d="M20 21v-3a4 4 0 0 1 8 0v3" fill="none" stroke="#777" stroke-width="1.4"/></svg>
    <div><h3>Retail</h3><p>Clothing, watches, jewelry, flowers and more!</p></div>
  </div>
  <div class="abs use-case uc-corporate">
    <svg viewBox="0 0 48 48"><use href="#ring"/><path d="M26 15h7v7L22 33l-7-7z" fill="none" stroke="#777" stroke-width="1.4" stroke-linejoin="round"/><circle cx="29.5" cy="18.5" r="1.5" fill="#777"/></svg>
    <div><h3>Corporate</h3><p>Product info, demonstration, information, brand awareness.</p></div>
  </div>
  <div class="abs use-case uc-fundraisers">
    <svg viewBox="0 0 48 48"><use href="#ring"/><rect x="17" y="20" width="14" height="14" fill="none" stroke="#777" stroke-width="1.4"/><path d="M24 31l-3.5-3.5a2 2 0 0 1 3.5-2.5a2 2 0 0 1 3.5 2.5z" fill="none" stroke="#777" stroke-width="1.2"/></svg>
    <div><h3>Fundraisers</h3><p>Girls/boy sports, non profits, etc</p></div>
  </div>

  <div class="abs divider divider-lower"></div>
  <div class="abs footer-bar"></div>
</main>
</body>
</html>
```